Website for Sports and Exercise Medicine Doctor with active research in stem cells therapies.

I am a sports and exercise medicine doctor with research interests in the cutting edge areas of biological therapies, most notable stem cells. None of my patients are dying of anything, and most of them come to see me to decrease their pain, so they can get back to what they want to do.

The approach i then take is to decrease their pain and support them to achieve the things they wish to achieve. Most people start at "Just make it stop hurting doc" , but I try to move them towards something more important over time.

I would like the website to be very different to other "Doctor or medical websites" in its look. No pictures of doctors in white coats and no pictures of fit old people smiling. I would potentially like the fist thing seen to be a quote:

"Less pain. Everybody wants it, but what are you going to do, once you've got it?"

(But this is only an idea, I am open to anything)

The website will need a couple of things

1. "Locations" I work
2. "Research" I am involved in
3. "Sort Me out" - Clinical information for people to access
4. "Social" - imbedded twitter and facebook
5. "Blog" - imbedded wordpress blog
6. "Bio" - the usual bio-stuff

The "Sort Me out" - pages I would like to have the functionality as seen in this site http://www.veltarion.com.au/platelet/. I intend to put disease topics into these pages (eg Achilles tehdinopathy, osteoarthritis etc etc etc). Once again I am not wedded to this but something along these lines would be good.

To give you an idea these are some sites I like
http://www.morbanquilt.com/
http://daptrine.com/
http://ovimbera.com.sg/
http://jolvaniketchup.com/
http://www.pilnorwave.com/
http://quadrisel.com/#offering
http://fennikstudio.tv/
http://norvalgate.com/
http://sablethorn.co.uk/#about

Target Market(s)

20-80 year old.
People with tendon injuries
People with osteoarthritis
People interested in stem cells
I will build the site over time to contain information on multiple sporting injuries and musculoskeletal disorders. It will also become a site for the latest on stem cell research particularly in the area of osteoarthritis.

Industry/Entity Type

Medical

Font styles to use
Sans Serif

Colors
ffffff

Requirements
Nice to have
• To give you an idea these are some sites I like
http://daptrine.com/
http://fennikstudio.tv/
http://norvalgate.com/
Should not have
• Pictures of doctors in white coats or old fit people smiling

```html
<!DOCTYPE html>
<html lang="en">
<head>
<meta charset="utf-8">
<title>halvor — Sports &amp; Exercise Medicine</title>
<link href="https://fonts.googleapis.com/css2?family=Lato:wght@300;400;700&display=swap" rel="stylesheet">
<style>
:root{
  --teal:#2e6e86;
  --teal-bar:#36778c;
  --ink:#3a3a3a;
  --body-text:#4a4a4a;
  --panel:#f2f2f2;
  --card-line:#e4e4e4;
  --footer:#3d3c42;
  --search:#5a5a5a;
  --white:#ffffff;
  --black:#050505;
}
*{margin:0;padding:0;box-sizing:border-box}
html,body{width:1200px;height:1188px;overflow:hidden;background:var(--white);font-family:'Lato',sans-serif}
.page{position:relative;width:1200px;height:1188px}
.brand{position:absolute;left:116px;top:38px;font-weight:300;font-size:58px;line-height:70px;color:var(--teal);letter-spacing:1px}
.search{position:absolute;left:907px;top:20px;width:180px;height:26px;background:var(--search);border:1px solid #6a6a6a}
.search span{position:absolute;left:10px;top:4px;font-size:14px;color:#e8e8e8}
.search .go{position:absolute;right:0;top:0;width:24px;height:24px;background:var(--teal)}
.nav{position:absolute;top:78px;left:0;width:1200px;list-style:none}
.nav li{position:absolute;font-size:12px;letter-spacing:1.6px;color:var(--ink)}
.nav .active::after{content:"";position:absolute;left:-3px;right:-3px;top:41px;height:5px;background:var(--teal)}
.hero{position:absolute;left:11px;top:127px;width:1177px;height:503px;overflow:hidden;
  background:radial-gradient(ellipse at 30% 25%,#f3d9a8 0%,#e6b36a 30%,transparent 60%),
  linear-gradient(180deg,#e9c287 0%,#d89550 45%,#b8552c 75%,#8a3a22 100%)}
.hero-copy{position:absolute;left:0;width:1177px;text-align:center;color:var(--white)}
.hero h1{position:absolute;top:215px;left:0;width:1177px;font-weight:300;font-size:43px;letter-spacing:-0.5px}
.hero .tag{position:absolute;top:272px;left:411px;width:396px;height:24px;background:var(--teal);font-weight:700;font-size:18px;line-height:24px}
.hero .cta{position:absolute;top:321px;left:531px;width:138px;height:31px;background:var(--black);border-bottom:3px solid var(--teal);font-size:18px;line-height:28px;letter-spacing:.5px}
.arrow{position:absolute;top:343px;width:33px;height:72px;background:var(--black)}
.arrow.left{left:11px}.arrow.right{left:1156px}
.arrow svg{position:absolute;left:8px;top:24px}
.services{position:absolute;left:11px;top:630px;width:1177px;height:359px;background:var(--panel)}
.card{position:absolute;top:35px;width:311px;height:287px;background:#fcfcfc;border:1px solid var(--card-line);text-align:center}
.card svg{position:absolute;left:125px;top:56px}
.card h2{position:absolute;top:145px;width:100%;font-weight:400;font-size:22px;color:var(--teal)}
.card p{position:absolute;top:198px;width:100%;padding:0 18px;font-weight:300;font-size:16px;line-height:19.5px;color:var(--body-text)}
.footer{position:absolute;left:11px;top:989px;width:1177px;height:152px;background:var(--footer)}
.footer .brand-foot{position:absolute;top:18px;width:100%;text-align:center;font-weight:300;font-size:58px;color:var(--white)}
.social{position:absolute;top:111px;width:30px;height:30px;background:var(--black)}
.legal{position:absolute;left:11px;top:1141px;width:1177px;height:32px;background:var(--teal-bar);color:var(--white);font-size:11px;font-weight:700}
.legal span{position:absolute;top:9px}
.legal u{font-weight:400}
</style>
</head>
<body>
<div class="page">
  <header>
    <div class="brand">halvor</div>
    <div class="search"><span>Search Me</span><div class="go">
      <svg width="24" height="24" viewBox="0 0 24 24"><circle cx="11" cy="11" r="3.5" fill="none" stroke="#fff" stroke-width="1.6"/><line x1="13.5" y1="13.5" x2="16" y2="16" stroke="#fff" stroke-width="1.8"/></svg>
    </div></div>
    <ul class="nav">
      <li class="active" style="left:375px">HOME</li>
      <li style="left:474px">ABOUT US</li>
      <li style="left:584px">RESEARCH</li>
      <li style="left:702px">SORT ME OUT</li>
      <li style="left:839px">BIO</li>
      <li style="left:912px">LOCATION</li>
      <li style="left:1026px">BLOG</li>
    </ul>
  </header>

  <section class="hero" role="img" aria-label="Close-up of a runner's red trainers striding along a sunlit road">
    <div class="hero-copy">
      <h1>LESS PAIN, EVERYBODY WANTS IT.</h1>
      <div class="tag">But what are you going to do, once you've got it?</div>
      <div class="cta">read more</div>
    </div>
  </section>
  <div class="arrow left"><svg width="16" height="24"><polyline points="12,2 3,12 12,22" fill="none" stroke="#fff" stroke-width="1.5"/></svg></div>
  <div class="arrow right"><svg width="16" height="24"><polyline points="4,2 13,12 4,22" fill="none" stroke="#fff" stroke-width="1.5"/></svg></div>

  <section class="services">
    <div class="card" style="left:99px">
      <svg width="60" height="64" viewBox="0 0 60 64" fill="#333">
        <rect x="8" y="56" width="40" height="5"/>
        <rect x="22" y="50" width="6" height="7"/>
        <rect x="26" y="8" width="9" height="24" transform="rotate(28 30 20)"/>
        <rect x="32" y="2" width="8" height="6" transform="rotate(28 36 5)"/>
        <path d="M38 28 a14 14 0 0 1 -10 24 h-16 v-4 h16 a10 10 0 0 0 6 -17z"/>
        <rect x="12" y="38" width="16" height="4"/>
      </svg>
      <h2>RESEARCH</h2>
      <p>Lorem ipsum dolor a sit eget amet, consectetur adipiscing elit in sit amet aliquet odio, nec vehicula leo.</p>
    </div>
    <div class="card" style="left:434px">
      <svg width="60" height="64" viewBox="0 0 60 64" fill="#333">
        <path d="M22 14 v-4 h16 v4 h-3 v-2 h-10 v2z"/>
        <rect x="3" y="14" width="54" height="38" rx="3"/>
        <rect x="3" y="30" width="54" height="2" fill="#fcfcfc"/>
        <rect x="24" y="26" width="12" height="12" rx="2" fill="#fcfcfc"/>
        <rect x="27" y="29" width="6" height="6" rx="1"/>
      </svg>
      <h2>SORT ME OUT</h2>
      <p>Lorem ipsum dolor a sit eget amet, consectetur adipiscing elit in sit amet aliquet odio, nec vehicula leo.</p>
    </div>
    <div class="card" style="left:764px">
      <svg width="60" height="64" viewBox="0 0 60 64" fill="none" stroke="#333" stroke-width="2.5">
        <path d="M10 6 h28 l6 6 v16 M10 6 v52 h32"/>
        <line x1="16" y1="18" x2="36" y2="18"/><line x1="16" y1="26" x2="36" y2="26"/><line x1="16" y1="34" x2="28" y2="34"/>
        <path d="M28 50 l20 -20 l6 6 l-20 20 l-8 2z" fill="#333"/>
      </svg>
      <h2>BIO</h2>
      <p>Lorem ipsum dolor a sit eget amet, consectetur adipiscing elit in sit amet aliquet odio, nec vehicula leo.</p>
    </div>
  </section>

  <footer class="footer">
    <div class="brand-foot">halvor</div>
    <div class="social" style="left:508px" aria-label="Social link"></div>
    <div class="social" style="left:561px" aria-label="Social link"></div>
    <div class="social" style="left:616px" aria-label="Social link"></div>
  </footer>
  <div class="legal">
    <span style="left:113px">Copyright 2013 - halvoris.com - All Rights Reserved</span>
    <span style="left:775px">Phone: +38 045 712-30-96</span>
    <span style="left:925px">E-mail: <u>support@halvoris.com</u></span>
  </div>
</div>
</body>
</html>
```